Wordpress Template Design using existing Logo and Colors

We are wanting a wordpress theme designing for our b2b marketing consultancy business. A comprehesive and elagant design to our current site www.provexlink.com would be good.

Industry/Entity Type

Marketing

Font styles to use
Sans Serif

```html
<!DOCTYPE html>
<html lang="en">
<head>
<meta charset="utf-8">
<title>Provexlink — Better Data, Better Target, Better Results</title>
<link rel="stylesheet" href="https://fonts.googleapis.com/css2?family=Montserrat:wght@400;500;600;700;800&family=Open+Sans:wght@400;600;700&display=swap">
<style>
:root{
  --red:#e8202a;
  --slate:#4e5769;
  --navy:#1c2031;
  --ink:#222633;
  --text:#555a66;
  --muted:#8a8f99;
  --mist:#f3f4f8;
  --white:#ffffff;
}
*{margin:0;padding:0;box-sizing:border-box}
html,body{width:1200px;height:2908px;overflow:hidden;background:var(--white)}
body{position:relative;font-family:'Open Sans',sans-serif;color:var(--text)}

/* header */
.site-header{position:absolute;left:0;top:0;width:1200px;height:78px;background:var(--white)}
.brand{position:absolute;display:flex;align-items:center;gap:10px;font-family:'Montserrat',sans-serif;font-weight:700;color:var(--red);letter-spacing:1px;line-height:1}
.brand .dot{width:12px;height:12px;background:var(--red)}
.site-header .brand{left:88px;top:24px;font-size:30px}
.main-nav{position:absolute;left:436px;top:30px;display:flex;gap:26px;font-family:'Montserrat',sans-serif;font-size:14px;font-weight:500;color:var(--ink)}
.support{position:absolute;right:56px;top:24px;display:flex;align-items:center;gap:8px;font-size:13px;color:var(--muted)}
.support strong{font-family:'Montserrat',sans-serif;font-size:20px;color:var(--ink);font-weight:600}

/* hero */
.hero{position:absolute;left:0;top:78px;width:1200px;height:584px;overflow:hidden}
.hero-photo{position:absolute;inset:0;background:linear-gradient(100deg,#5c6470 0%,#3a3c42 40%,#1f1f23 100%)}
.hero-slant{position:absolute;left:0;bottom:0;width:1200px;height:70px}
.hero-copy{position:absolute;left:620px;top:170px;width:560px;color:var(--white)}
.hero-copy h1{font-family:'Montserrat',sans-serif;font-weight:700;font-size:34px;line-height:42px}
.hero-copy p{margin-top:22px;font-size:14px;line-height:24px;font-weight:600}
.btn{display:inline-flex;align-items:center;justify-content:center;background:var(--red);color:var(--white);font-family:'Montserrat',sans-serif;font-weight:500}
.hero-copy .btn{margin-top:24px;width:142px;height:42px;font-size:14px}

/* welcome */
.mist{position:absolute;left:0;top:600px;width:1200px;height:840px;background:var(--mist);clip-path:polygon(0 62px,100% 0,100% 100%,0 89%)}
.welcome-title{position:absolute;left:128px;top:708px;text-align:center;font-family:'Montserrat',sans-serif;font-weight:700;color:var(--slate)}
.welcome-title .big{font-size:46px;letter-spacing:1px;line-height:52px}
.welcome-title .small{font-size:32px;line-height:40px}
.welcome-title .small b{color:var(--red)}
.welcome-rule{position:absolute;left:430px;top:714px;width:2px;height:104px;background:#c8cbd2}
.welcome-text{position:absolute;left:470px;top:714px;width:612px;font-size:14.5px;line-height:27px}

/* services */
.card{position:absolute;width:486px;height:160px;background:var(--white);border:1px solid #e1e3e8}
.card .thumb{position:absolute;left:0;top:14px;width:140px;height:132px;border:6px solid var(--white);box-shadow:0 1px 4px rgba(0,0,0,.15)}
.card h3{position:absolute;left:170px;top:30px;font-family:'Montserrat',sans-serif;font-weight:600;font-size:19px;color:var(--ink);letter-spacing:.3px}
.card p{position:absolute;left:170px;top:62px;width:296px;font-size:13px;line-height:21px}
.card.active{background:transparent;border:none}
.card.active .panel{position:absolute;left:112px;top:0;width:374px;height:160px;background:var(--slate)}
.card.active .thumb{border-color:var(--red);box-shadow:none}
.card.active h3,.card.active p{color:var(--white)}

/* data management */
.dm-art{position:absolute;left:68px;top:1474px;width:470px;height:520px;background:linear-gradient(90deg,#5a6273 0%,#c7434a 35%,#4e5769 60%,#d9dbe0 100%)}
.dm-copy{position:absolute;left:620px;top:1496px;width:470px}
.dm-copy h2{font-family:'Montserrat',sans-serif;font-weight:700;font-size:36px;color:var(--ink);letter-spacing:.5px}
.dm-copy h4{margin-top:22px;font-family:'Montserrat',sans-serif;font-weight:600;font-size:19px;line-height:27px;color:var(--red)}
.dm-copy p{margin-top:22px;font-size:13px;line-height:21px}

/* brochure */
.brochure{position:absolute;left:0;top:1994px;width:1200px;height:126px;background:var(--navy);color:var(--white)}
.brochure h2{position:absolute;left:87px;top:24px;font-family:'Montserrat',sans-serif;font-weight:500;font-size:30px;letter-spacing:1px}
.brochure p{position:absolute;left:87px;top:66px;width:660px;font-size:13px;line-height:20px}
.brochure .btn{position:absolute;left:855px;top:41px;width:253px;height:54px;border-radius:4px;font-size:17px;gap:10px}

/* testimonials */
.reviews-title{position:absolute;left:0;top:2196px;width:1200px;text-align:center;font-family:'Montserrat',sans-serif;font-weight:700;font-size:30px;color:var(--ink)}
.avatar{position:absolute;left:560px;top:2269px;width:86px;height:86px;border-radius:50%;background:linear-gradient(180deg,#d9d4cf,#b9b1aa);border:4px solid #eee}
.quote{position:absolute;left:260px;top:2380px;width:680px;text-align:center;font-size:13px;line-height:22px;color:var(--muted)}
.author{position:absolute;left:0;top:2462px;width:1200px;text-align:center;font-size:12.5px;color:var(--muted)}
.author b{color:var(--ink);font-weight:700}
.dots{position:absolute;left:586px;top:2510px;display:flex;gap:6px}
.dots span{width:8px;height:8px;border-radius:50%;background:#cfd1d6}
.dots span.on{background:#9a9ea6}

/* footer */
.site-footer{position:absolute;left:0;top:2572px;width:1200px;height:336px;background:var(--navy);color:var(--white)}
.site-footer .brand{left:107px;top:84px;font-size:32px}
.footer-about{position:absolute;left:107px;top:150px;width:290px;font-size:13px;line-height:21px}
.socials{position:absolute;left:110px;top:240px;display:flex;gap:20px}
.socials span{width:14px;height:14px;border-radius:50%;background:var(--red)}
.footer-col h5{position:absolute;font-family:'Montserrat',sans-serif;font-weight:500;font-size:21px}
.links{position:absolute;list-style:none;font-family:'Montserrat',sans-serif;font-weight:600;font-size:12px;letter-spacing:.5px}
.links li{height:33px}
.contact{position:absolute;left:840px;list-style:none;font-size:13px;line-height:20px}
.contact li{display:flex;gap:18px;margin-bottom:28px}
.contact svg{flex:none;margin-top:3px}
.footer-rule{position:absolute;left:107px;top:280px;width:986px;height:1px;background:#33384a}
.copyright{position:absolute;left:0;top:300px;width:1200px;text-align:center;font-size:13px}
</style>
</head>
<body>

<header class="site-header">
  <div class="brand"><span>Provexlink</span><span class="dot"></span></div>
  <nav class="main-nav"><span>TARGET MARKETING</span><span>DATA MANAGEMENT</span><span>ABOUT</span></nav>
  <div class="support">
    <svg width="18" height="18" viewBox="0 0 18 18"><rect width="18" height="18" rx="3" fill="#e8202a"/><path d="M5 4.5l2 0 1 3-1.3 1a6 6 0 0 0 2.8 2.8l1-1.3 3 1v2a1 1 0 0 1-1 1A9 9 0 0 1 4 5.5a1 1 0 0 1 1-1z" fill="#fff"/></svg>
    <span>24/7 support</span><strong>555-014-2290</strong>
  </div>
</header>

<section class="hero">
  <div class="hero-photo" role="img" aria-label="Smiling professional working on a laptop in a busy office"></div>
  <svg class="hero-slant" viewBox="0 0 1200 70" preserveAspectRatio="none"><polygon points="0,70 1200,0 1200,70" fill="#f3f4f8"/></svg>
  <div class="hero-copy">
    <h1>Better Data, Better Target,<br>Better Results</h1>
    <p>Delve into the behaviours of your most receptive and profitable<br>customers through sophisticated profiling programs.</p>
    <span class="btn">Learn More</span>
  </div>
</section>

<div class="mist"></div>

<section class="welcome">
  <div class="welcome-title"><div class="big">WELCOME</div><div class="small">to <b>Provex</b>link</div></div>
  <div class="welcome-rule"></div>
  <p class="welcome-text">We are a B2B Data, Analytics and Marketing Consulting Company specialized in harnessing the power of potential data to strengthen connections between decisions makers, companies and products. We focus on solutions engineered to solve distinct challenges in the data, direct marketing, and analytics space.</p>
</section>

<section class="services">
  <article class="card active" style="left:100px;top:904px">
    <div class="panel"></div>
    <div class="thumb" style="background:linear-gradient(135deg,#9ea8b6,#5d6676)" role="img" aria-label="Hand holding a tablet showing a network of connected people"></div>
    <h3>B2B DATABASE</h3>
    <p>Get access to Asia's leading market &amp; business intelligence database over 1,500,000 organizations and 3,500,000 decision makers.</p>
  </article>
  <article class="card" style="left:611px;top:904px">
    <div class="thumb" style="background:linear-gradient(135deg,#c9484c,#4a4e5a)" role="img" aria-label="Businessman holding a red and white target"></div>
    <h3>TARGET MARKETING</h3>
    <p>We develop tailored marketing solutions based on your specific objectives, audience and budget to fetch high returns on investment.</p>
  </article>
  <article class="card" style="left:100px;top:1102px">
    <div class="thumb" style="background:linear-gradient(135deg,#d7dbe0,#6f7784)" role="img" aria-label="Call centre agents wearing headsets"></div>
    <h3>CALL CENTRE</h3>
    <p>When your business requires instantaneous and cost effective contact center, we are here to provide the necessary expertise.</p>
  </article>
  <article class="card" style="left:611px;top:1102px">
    <div class="thumb" style="background:linear-gradient(135deg,#e3e6e9,#c04a4d)" role="img" aria-label="Magnifying glass over a padlock and data label"></div>
    <h3>DATA MANAGEMENT</h3>
    <p>We analyze your data and report on effective strategies for turning the data into a profitable resource.</p>
  </article>
</section>

<section class="data-management">
  <div class="dm-art" role="img" aria-label="Illustration of a celebrating businessman in front of tall labelled columns for the data management steps"></div>
  <div class="dm-copy">
    <h2>DATA MANAGEMENT</h2>
    <h4>We analyze your data and report on effective strategies for turning the data into a profitable resource.</h4>
    <p>Many organisations hold valuable customer data but they cannot put it to effective and profitable use due to inefficient processes and invalid data. In a good database, data is accurate, up-to-date and formatted consistently. However, inaccurate, misspelling, duplication, incompleteness and use of incorrect data formats can occur in a database especially when there were no rigorous control for data inputs.</p>
    <p>Success of every marketing or customer communication efforts will be dependent on the quality of the data that organisation hold in their database. At Provexlink, data services are our core business and our clients are companies that use data for Direct Marketing or CRM purposes or as an Information Source. With our sophisticated technology solutions, we offer hassle free, expert services for all your data needs from Data Quality Audit to Data Management Services.</p>
  </div>
</section>

<section class="brochure">
  <h2>CORPORATE BROCHURE</h2>
  <p>Learn our leading target marketing and intelligent data management solutions to attain new customers for your niche products and services.</p>
  <span class="btn">Download Now
    <svg width="18" height="18" viewBox="0 0 18 18" fill="#fff"><path d="M7.5 1h3v7h3l-4.5 5-4.5-5h3z"/><rect x="1" y="13" width="2" height="4"/><rect x="15" y="13" width="2" height="4"/><rect x="1" y="15" width="16" height="2"/></svg>
  </span>
</section>

<section class="reviews">
  <h2 class="reviews-title">WHY CUSTOMERS
    <svg width="30" height="27" viewBox="0 0 30 27" style="vertical-align:-3px"><path d="M15 27L2.5 14A7.5 7.5 0 0 1 15 4a7.5 7.5 0 0 1 12.5 10z" fill="#e8202a"/></svg>
  US!</h2>
  <div class="avatar" role="img" aria-label="Portrait of the reviewer"></div>
  <p class="quote">Lorem ipsum is that it has a more-or-less normal distribution of letters, as opposed to using content here now use Lorem Ipsum as their default model text, and a search for lorem ipsum will uncover many web sites still in their infancy various versions have evolved over the years.</p>
  <p class="author"><b>- Marissa Teller</b> &nbsp;<i>- CEO and Founder</i></p>
  <div class="dots"><span></span><span class="on"></span><span></span></div>
</section>

<footer class="site-footer">
  <div class="brand"><span>Provexlink</span><span class="dot"></span></div>
  <p class="footer-about">Dummy text of the printing and typesetting industry. Lorem Ipsum has been the industry's standard dummy text ever</p>
  <div class="socials"><span></span><span></span><span></span><span></span><span></span><span></span></div>
  <div class="footer-col">
    <h5 style="left:442px;top:46px">Useful Links</h5>
    <ul class="links" style="left:442px;top:96px"><li>HOME</li><li>ABOUT</li><li>TRAINING</li><li>BUSINESS ADVISORY</li><li>CONSULTING</li></ul>
    <ul class="links" style="left:638px;top:92px"><li>SKILLS TESTING</li><li>NEWS &amp; VIEWS</li><li>CONTACT US</li></ul>
  </div>
  <div class="footer-col">
    <h5 style="left:840px;top:46px">Contact Us</h5>
    <ul class="contact" style="top:100px">
      <li><svg width="14" height="14" viewBox="0 0 14 14" fill="#8a8f99"><path d="M7 1L1 6h2v7h3V9h2v4h3V6h2z"/></svg><span>Level 3 / 42 Harbour Lane, MARLOW<br>NSW 2099 AUSTRALIA</span></li>
      <li><svg width="14" height="14" viewBox="0 0 14 14" fill="#8a8f99"><path d="M3 1h2.5l1 3-1.5 1.2a7 7 0 0 0 3.8 3.8L10 7.5l3 1V11a1.5 1.5 0 0 1-1.5 1.5A10.5 10.5 0 0 1 1.5 2.5 1.5 1.5 0 0 1 3 1z"/></svg><span>+ 61 (0) 2 5550-1934</span></li>
      <li><svg width="14" height="14" viewBox="0 0 14 14" fill="#8a8f99"><rect x="1" y="3" width="12" height="9" rx="1"/><path d="M1.5 3.5L7 8l5.5-4.5" stroke="#1c2031" stroke-width="1.3" fill="none"/></svg><span>hello@provexlink.com</span></li>
    </ul>
  </div>
  <div class="footer-rule"></div>
  <p class="copyright">Copyright © 2017, provexlink. Privacy Policy Terms &amp; Conditions</p>
</footer>

</body>
</html>
```